Business Card Design for The Lending Nook Inc.

We need a business card design for our mortgage company: "The Lending Nook Inc."

Need to have Social Media Account on there as a possibility

Industry/Entity Type

Business

```html
<!DOCTYPE html>
<html lang="en">
<head>
<meta charset="utf-8">
<title>The Lending Nook Inc. – Business Card</title>
<link href="https://fonts.googleapis.com/css2?family=Arimo:wght@700&family=PT+Sans+Narrow&family=Quicksand:wght@500&display=swap" rel="stylesheet">
<style>
  :root {
    --page: #ffffff;
    --card: #0b0b0b;
    --card-glow: #1c1c1c;
    --brand-blue: #1565b5;
    --text-light: #c9c9c9;
    --text-mid: #a8a8a8;
    --divider: #050505;
    --social-a: #1d9ff0;
    --social-b: #3a5a9a;
    --social-c: #2f7bc0;
  }
  html, body {
    margin: 0;
    width: 1200px;
    height: 1200px;
    overflow: hidden;
    background: var(--page);
  }
  .card {
    position: absolute;
    left: 202px;
    width: 840px;
    height: 480px;
    background:
      radial-gradient(ellipse 360px 260px at 440px 240px, var(--card-glow), transparent 70%),
      var(--card);
    overflow: hidden;
  }
  .card--front { top: 62px; }
  .card--back { top: 600px; }

  .brand {
    position: absolute;
    left: 140px;
    top: 64px;
    display: flex;
    align-items: center;
    gap: 18px;
  }
  .brand__dot {
    width: 58px;
    height: 58px;
    border-radius: 50%;
    border: 5px solid var(--brand-blue);
    box-sizing: border-box;
  }
  .brand__name {
    font-family: "Arimo", sans-serif;
    font-weight: 700;
    font-size: 44px;
    color: var(--brand-blue);
    letter-spacing: -0.5px;
    white-space: nowrap;
  }

  .divider {
    position: absolute;
    left: 452px;
    top: 156px;
    width: 4px;
    height: 200px;
    background: linear-gradient(to bottom, transparent, var(--divider) 20%, var(--divider) 80%, transparent);
  }

  .company {
    position: absolute;
    right: 410px;
    top: 208px;
    text-align: right;
  }
  .company__name {
    font-family: "PT Sans Narrow", sans-serif;
    font-size: 33px;
    letter-spacing: -1px;
    color: var(--text-light);
    line-height: 1;
  }
  .company__web {
    font-family: "Quicksand", sans-serif;
    font-size: 15px;
    letter-spacing: 1.5px;
    color: var(--text-mid);
    margin-top: 6px;
  }
  .initials {
    position: absolute;
    left: 476px;
    top: 176px;
    font-family: "Arimo", sans-serif;
    font-size: 128px;
    line-height: 1;
    background: linear-gradient(to bottom, #dcdcdc, #8a8a8a);
    -webkit-background-clip: text;
    background-clip: text;
    color: transparent;
  }

  .contact {
    position: absolute;
    right: 398px;
    top: 174px;
    margin: 0;
    padding: 0;
    list-style: none;
    text-align: right;
    font-family: "Quicksand", sans-serif;
    font-size: 16px;
    letter-spacing: 0.6px;
    color: var(--text-mid);
  }
  .contact li { height: 33px; line-height: 20px; }

  .icons {
    position: absolute;
    left: 470px;
    top: 170px;
  }

  .person {
    position: absolute;
    left: 532px;
    top: 212px;
    font-family: "Quicksand", sans-serif;
    color: var(--text-mid);
  }
  .person__name { font-size: 19px; letter-spacing: 0.4px; }
  .person__role { font-size: 16px; margin-top: 4px; }
</style>
</head>
<body>

<section class="card card--front">
  <div class="brand">
    <span class="brand__dot"></span>
    <span class="brand__name">The Lending Nook Inc.</span>
  </div>
  <div class="divider"></div>
  <div class="company">
    <div class="company__name">Lending Nook Inc</div>
    <div class="company__web">WWW.WEBPAGE.COM</div>
  </div>
  <div class="initials">LN</div>
</section>

<section class="card card--back">
  <div class="brand">
    <span class="brand__dot"></span>
    <span class="brand__name">The Lending Nook Inc.</span>
  </div>
  <div class="divider"></div>

  <ul class="contact">
    <li>555 888 555</li>
    <li>1420 Elm Avenue Fresno, CA 93700</li>
    <li>Yourmail@webpage.com</li>
    <li>Chirper.com/YourName</li>
  </ul>

  <svg class="icons" width="40" height="220" viewBox="0 0 40 220" aria-hidden="true">
    <!-- phone -->
    <g fill="#a8a8a8">
      <path d="M6 12 q10 -8 24 0 v4 h-6 v-3 q-6 -2 -12 0 v3 h-6z"/>
      <rect x="9" y="16" width="18" height="9" rx="2"/>
    </g>
    <circle cx="18" cy="20" r="2.5" fill="#0b0b0b"/>
    <!-- pin -->
    <path d="M18 36 a8 8 0 0 1 8 8 c0 6 -8 14 -8 14 s-8 -8 -8 -14 a8 8 0 0 1 8 -8z" fill="#a8a8a8"/>
    <circle cx="18" cy="44" r="3" fill="#0b0b0b"/>
    <!-- mail -->
    <rect x="6" y="74" width="24" height="15" fill="#a8a8a8"/>
    <path d="M6 74 l12 9 l12 -9" fill="none" stroke="#0b0b0b" stroke-width="1.5"/>
    <!-- social placeholders -->
    <circle cx="18" cy="118" r="14" fill="var(--social-a)"/>
    <circle cx="18" cy="158" r="14" fill="var(--social-b)"/>
    <circle cx="18" cy="200" r="14" fill="var(--social-c)"/>
  </svg>

  <div class="person">
    <div class="person__name">YOUR NAME</div>
    <div class="person__role">YOUR JOB</div>
  </div>
</section>

</body>
</html>
```